Mindfulness School for Children -- Business Cards

We're looking for business cards for our school directors and owners. We're a mindfulness school for children called tumbling willows. Attached are our logos/icons.

```html
<!DOCTYPE html>
<html lang="en">
<head>
<meta charset="utf-8">
<title>Tumbling Willows – Business Cards</title>
<link rel="stylesheet" href="https://fonts.googleapis.com/css2?family=Arimo:wght@400;700&display=swap">
<style>
  :root {
    --stage: #e9e9e7;
    --card: #232323;
    --ink: #f2f2f2;
    --teal: #6fbfcf;
    --green: #8fcf9f;
    --mint: #c8ead0;
    --rule: #6fb7a8;
  }
  * { box-sizing: border-box; margin: 0; padding: 0; }
  html, body { width: 1200px; height: 900px; overflow: hidden; }
  body {
    background: var(--stage);
    font-family: "Arimo", Arial, sans-serif;
    position: relative;
  }
  .card {
    position: absolute;
    left: 300px;
    width: 600px;
    height: 343px;
    border-radius: 18px;
    background: var(--card);
    overflow: hidden;
    box-shadow: 0 10px 28px rgba(0,0,0,.22);
  }
  .card--front { top: 70px; }
  .card--back { top: 477px; }

  .card__edge {
    position: absolute;
    left: 0; right: 0; bottom: 0;
    height: 7px;
    background: linear-gradient(90deg, var(--teal), var(--green) 45%, var(--mint) 75%, var(--teal));
  }
  .brand {
    position: absolute;
    left: 44px; top: 118px;
    width: 250px;
    display: flex; align-items: flex-start; gap: 10px;
  }
  .brand__dot {
    width: 14px; height: 14px; border-radius: 50%;
    background: var(--teal);
    margin-top: 14px;
    flex: none;
  }
  .brand__name {
    font-size: 34px; font-weight: 400;
    line-height: 1.1;
    color: var(--teal);
    letter-spacing: .5px;
  }
  .brand__line { display: block; }
  .brand__line--second { margin-left: 72px; }
  .divider {
    position: absolute;
    left: 318px; top: 70px;
    width: 1px; height: 200px;
    background: var(--rule);
  }
  .contact {
    position: absolute;
    left: 342px; top: 78px;
    color: var(--ink);
  }
  .contact__name {
    font-size: 22px; font-weight: 700;
    color: var(--teal);
    letter-spacing: .5px;
  }
  .contact__role { font-size: 14px; margin: 2px 0 14px; }
  .contact__list { list-style: none; font-size: 14px; line-height: 23px; }
  .contact__list li { display: flex; align-items: center; gap: 7px; }
  .contact__list svg { width: 12px; height: 12px; flex: none; fill: var(--teal); }
  .contact__address { font-size: 14px; line-height: 20px; margin-top: 8px; }

  .pattern-fill {
    position: absolute; inset: 0;
    background: linear-gradient(120deg, #1a1a1a 0%, #262626 45%, #5a5a5a 80%, #8c8c8c 100%);
  }
</style>
</head>
<body>
  <section class="card card--front">
    <div class="brand">
      <span class="brand__dot"></span>
      <span class="brand__name">
        <span class="brand__line">tumbling</span>
        <span class="brand__line brand__line--second">willows</span>
      </span>
    </div>
    <div class="divider"></div>
    <div class="contact">
      <h1 class="contact__name">MARA ELLISON</h1>
      <p class="contact__role">CEO/Founder</p>
      <ul class="contact__list">
        <li><svg viewBox="0 0 24 24"><path d="M6.6 10.8a15.1 15.1 0 0 0 6.6 6.6l2.2-2.2a1 1 0 0 1 1-.25 11.4 11.4 0 0 0 3.6.57 1 1 0 0 1 1 1V20a1 1 0 0 1-1 1A17 17 0 0 1 3 4a1 1 0 0 1 1-1h3.5a1 1 0 0 1 1 1c0 1.250.2 2.45.57 3.57a1 1 0 0 1-.25 1z"/></svg>(00) 5281 3960</li>
        <li><svg viewBox="0 0 24 24"><path d="M2 5h20v14H2z M2 5l10 8 10-8" fill="none" stroke="#6fbfcf" stroke-width="2"/></svg>info@tumblingwillows.com</li>
        <li><svg viewBox="0 0 24 24"><circle cx="12" cy="12" r="9" fill="none" stroke="#6fbfcf" stroke-width="2"/><path d="M3 12h18M12 3c3 3 3 15 0 18M12 3c-3 3-3 15 0 18" fill="none" stroke="#6fbfcf" stroke-width="1.6"/></svg>www.tumblingwillows.com</li>
      </ul>
      <p class="contact__address">Po Box 4120 Brook Lane<br>Country Name, AB 60318</p>
    </div>
    <div class="card__edge"></div>
  </section>

  <section class="card card--back">
    <div class="pattern-fill" role="img" aria-label="Repeating lotus flower pattern fading from black to silver, with a single blue lotus accent"></div>
  </section>
</body>
</html>
```